Velmora professional haircare products

I started a unisex haircare line. It’s a modern organic unisex haircare line that focuses on looking appealing to both sexes. I like to keep it sexy modern and sleek but yet interesting. Right now my product consists of 8 products that I’d like to consider as one look. I’d like to relaunch a different styling section of my line with a new look that look similar but yet look like an elite different line within the company. I’m going to be focusing on hair gel, hair putty, beard oil, and body washes. I want to appeal to men and women equally.
Updates

Please help submit ideas?

Industry/Entity Type

Hair And Beauty

Requirements
Must have
• I want to utilize some color but maybe no more then 3 color that compliment each other. I want to still use my logo for the middle of my bottles just looking for creative graphic design around the bottle to change up the look.
Nice to have
• I would like to see graphic design. Some interesting bottles. Maybe with unisex floral designs combined with modern colors. I’m into the subtle nude color scales. Light the pastels or muted color tones. I wanna see moment and flow
Should not have
• I do not want it to look childish

```html
<!DOCTYPE html>
<html lang="en">
<head>
<meta charset="utf-8">
<title>Velmora Professional Hair Gel Label</title>
<link href="https://fonts.googleapis.com/css2?family=Montserrat:wght@200;300;500;700&display=swap" rel="stylesheet">
<style>
  :root {
    --page: #ffffff;
    --label-dark: #121513;
    --leaf-deep: #1f4a37;
    --leaf-mid: #3d8a66;
    --leaf-light: #7cc4a0;
    --silver: #d4d6d5;
    --silver-dim: #b9bcbb;
    --line: #f4f6f5;
  }
  html, body {
    margin: 0;
    padding: 0;
    width: 1200px;
    height: 1200px;
    overflow: hidden;
    background: var(--page);
  }
  .canvas {
    position: relative;
    width: 1200px;
    height: 1200px;
  }
  .label {
    position: absolute;
    left: 308px;
    top: 80px;
    width: 584px;
    height: 1040px;
    overflow: hidden;
    background: var(--label-dark);
    font-family: "Montserrat", sans-serif;
    color: var(--silver);
  }
  .label__foliage {
    position: absolute;
    inset: 0;
    background:
      radial-gradient(ellipse 38% 34% at 50% 54%, rgba(18,21,19,0.96) 0%, rgba(18,21,19,0.85) 55%, rgba(18,21,19,0) 100%),
      radial-gradient(circle at 15% 12%, var(--leaf-light) 0%, rgba(124,196,160,0) 30%),
      radial-gradient(circle at 88% 35%, var(--leaf-light) 0%, rgba(124,196,160,0) 28%),
      radial-gradient(circle at 12% 88%, var(--leaf-light) 0%, rgba(124,196,160,0) 26%),
      radial-gradient(circle at 82% 90%, var(--leaf-mid) 0%, rgba(61,138,102,0) 30%),
      linear-gradient(160deg, var(--leaf-mid) 0%, var(--leaf-deep) 45%, var(--leaf-mid) 100%);
  }
  .label__frames {
    position: absolute;
    inset: 0;
  }
  .brand {
    position: absolute;
    left: 0;
    right: 0;
    top: 250px;
    text-align: center;
  }
  .brand__dot {
    display: block;
    width: 44px;
    height: 44px;
    margin: 0 auto 22px;
    border: 2px solid var(--silver-dim);
    border-radius: 50%;
  }
  .brand__name {
    margin: 0;
    font-weight: 300;
    font-size: 50px;
    line-height: 1;
    letter-spacing: 1px;
    text-transform: uppercase;
    color: var(--silver);
  }
  .brand__tier {
    margin: 8px 0 0;
    font-weight: 500;
    font-size: 19px;
    letter-spacing: 5px;
    color: var(--silver-dim);
  }
  .product {
    position: absolute;
    left: 0;
    right: 0;
    text-align: center;
    margin: 0;
  }
  .product__type {
    top: 418px;
    font-weight: 200;
    font-size: 124px;
    line-height: 1;
    letter-spacing: 4px;
  }
  .product__kind {
    top: 546px;
    font-weight: 700;
    font-size: 78px;
    line-height: 1;
    letter-spacing: 2px;
  }
  .product__audience {
    top: 630px;
    font-weight: 300;
    font-size: 22px;
    letter-spacing: 8px;
    text-transform: uppercase;
    color: var(--silver-dim);
  }
  .badges {
    position: absolute;
    left: 0;
    right: 0;
    top: 671px;
    display: flex;
    justify-content: center;
    gap: 24px;
  }
  .badge {
    width: 92px;
    height: 92px;
    border-radius: 50%;
    border: 3px solid var(--silver);
    box-sizing: border-box;
    background: rgba(18,21,19,0.6);
  }
  .product__volume {
    top: 798px;
    font-weight: 500;
    font-size: 19px;
    color: var(--silver);
  }
</style>
</head>
<body>
<div class="canvas">
  <div class="label">
    <div class="label__foliage" role="img" aria-label="Tropical monstera and palm leaf illustration in muted greens surrounding a dark centre"></div>
    <svg class="label__frames" width="584" height="1040" viewBox="0 0 584 1040" aria-hidden="true">
      <polygon points="366,55 582,432 468,944 201,995 14,682 105,148" fill="none" stroke="var(--line)" stroke-width="2.5"/>
      <polygon points="127,114 417,182 565,716 332,955 59,830 31,284" fill="none" stroke="var(--line)" stroke-width="2.5"/>
    </svg>

    <div class="brand">
      <span class="brand__dot"></span>
      <p class="brand__name">Velmora</p>
      <p class="brand__tier">PROFESSIONAL</p>
    </div>

    <h1 class="product product__type">HAIR</h1>
    <p class="product product__kind">GEL</p>
    <p class="product product__audience">Man &amp; Woman</p>

    <div class="badges">
      <span class="badge"></span>
      <span class="badge"></span>
      <span class="badge"></span>
    </div>

    <p class="product product__volume">5.5fl.oz 150ml</p>
  </div>
</div>
</body>
</html>
```